Business card for utility of the future

I need a business card template designed for brivolo. We provide sustainable water, energy and waste services to homes.

The card should include name, position, email address, phone number, website and our logo (attached). I would like it to convey professionalism and creativity.

Target Market(s)

Homeowners, investors, corporate partners.

Industry/Entity Type

Utility

Contact Information for Business Card

The card should include name, position, email address, phone number, website and our logo (attached).

```html
<!DOCTYPE html>
<html lang="en">
<head>
<meta charset="utf-8">
<title>brivolo business card</title>
<link rel="stylesheet" href="https://fonts.googleapis.com/css2?family=Arimo:wght@400;700&display=swap">
<style>
  :root {
    --backdrop: #2c2c2c;
    --card-green: #6cbf84;
    --brand-green: #3f9b5e;
    --accent-orange: #d4622e;
    --card-white: #f7f7f7;
    --ink: #1e1e1e;
    --on-green: #ffffff;
  }
  * { margin: 0; padding: 0; box-sizing: border-box; }
  html, body {
    width: 1200px;
    height: 997px;
    overflow: hidden;
    background: var(--backdrop);
    font-family: "Arimo", Arial, sans-serif;
  }
  .sheet {
    width: 1200px;
    height: 997px;
    display: flex;
    align-items: center;
    justify-content: center;
    gap: 60px;
  }
  .card {
    position: relative;
    width: 520px;
    height: 318px;
    border-radius: 18px;
    box-shadow: 0 18px 40px rgba(0,0,0,0.45);
    overflow: hidden;
  }
  .card--front {
    background: linear-gradient(160deg, #74c78b 0%, var(--card-green) 60%, #62b57a 100%);
    display: flex;
    align-items: center;
    justify-content: center;
  }
  .wordmark {
    font-family: "Arimo", Arial, sans-serif;
    font-weight: 700;
    letter-spacing: -1px;
    line-height: 1;
  }
  .card--front .wordmark {
    color: var(--on-green);
    font-size: 96px;
  }
  .card--back { background: var(--card-white); }
  .card--back .brand {
    position: absolute;
    top: 30px;
    right: 36px;
  }
  .card--back .wordmark {
    color: var(--brand-green);
    font-size: 54px;
  }
  .holder {
    position: absolute;
    left: 36px;
    top: 124px;
  }
  .holder-name {
    color: var(--brand-green);
    font-size: 17px;
    letter-spacing: 0.3px;
    text-transform: uppercase;
  }
  .holder-role {
    color: var(--ink);
    font-size: 11px;
    font-weight: 700;
    letter-spacing: 0.4px;
    text-transform: uppercase;
    margin-top: 3px;
  }
  .divider {
    position: absolute;
    left: 196px;
    right: 36px;
    top: 146px;
    height: 1px;
    background: var(--brand-green);
  }
  .contacts {
    position: absolute;
    left: 36px;
    top: 180px;
    list-style: none;
  }
  .contacts li {
    display: flex;
    align-items: flex-start;
    gap: 10px;
    color: var(--ink);
    font-size: 13px;
    line-height: 16px;
    margin-bottom: 8px;
  }
  .contact-icon {
    flex: none;
    width: 16px;
    height: 16px;
  }
  .website {
    position: absolute;
    right: 36px;
    top: 192px;
    color: var(--accent-orange);
    font-size: 14px;
    font-weight: 700;
    letter-spacing: 1.2px;
  }
</style>
</head>
<body>
<main class="sheet">
  <section class="card card--front" aria-label="Card front">
    <span class="wordmark">brivolo</span>
  </section>

  <section class="card card--back" aria-label="Card back">
    <div class="brand">
      <span class="wordmark">brivolo</span>
    </div>

    <div class="holder">
      <p class="holder-name">Lena Hartwell</p>
      <p class="holder-role">Founder &amp; CEO</p>
    </div>
    <div class="divider"></div>

    <ul class="contacts">
      <li>
        <svg class="contact-icon" viewBox="0 0 16 16" aria-hidden="true">
          <circle cx="8" cy="8" r="8" fill="#3f9b5e"/>
          <path d="M4 6.2c0-1 3.4-1.8 4-1.8s4 .8 4 1.8v1H10.2V6.3H5.8v.9H4z" fill="#fff"/>
          <rect x="5.2" y="7.8" width="5.6" height="3.4" rx="0.8" fill="#fff"/>
        </svg>
        <span>0412 555 019 / +61 412 555 019</span>
      </li>
      <li>
        <svg class="contact-icon" viewBox="0 0 16 16" aria-hidden="true">
          <circle cx="8" cy="8" r="8" fill="#3f9b5e"/>
          <rect x="4" y="5.2" width="8" height="5.6" rx="0.6" fill="#fff"/>
          <path d="M4.3 5.6 8 8.4l3.7-2.8" fill="none" stroke="#3f9b5e" stroke-width="0.9"/>
        </svg>
        <span>info@brivolo.com</span>
      </li>
      <li>
        <svg class="contact-icon" viewBox="0 0 16 16" aria-hidden="true">
          <circle cx="8" cy="8" r="8" fill="#3f9b5e"/>
          <path d="M4.2 5.4a1 1 0 0 1 1-1h5.6a1 1 0 0 1 1 1v3.6a1 1 0 0 1-1 1H7.4L5.4 11.6V10h-.2a1 1 0 0 1-1-1z" fill="#fff"/>
          <circle cx="6.2" cy="7.2" r="0.6" fill="#3f9b5e"/>
          <circle cx="8" cy="7.2" r="0.6" fill="#3f9b5e"/>
          <circle cx="9.8" cy="7.2" r="0.6" fill="#3f9b5e"/>
        </svg>
        <span>Lena.brivolo</span>
      </li>
      <li>
        <svg class="contact-icon" viewBox="0 0 16 16" aria-hidden="true">
          <circle cx="8" cy="8" r="8" fill="#3f9b5e"/>
          <path d="M8 3.6a2.8 2.8 0 0 0-2.8 2.8C5.2 8.6 8 12.4 8 12.4s2.8-3.8 2.8-6A2.8 2.8 0 0 0 8 3.6z" fill="#fff"/>
          <circle cx="8" cy="6.4" r="1.1" fill="#3f9b5e"/>
        </svg>
        <span>PO Box 2208<br>Northgate QLD 4013</span>
      </li>
    </ul>

    <p class="website">www.brivolo.com</p>
  </section>
</main>
</body>
</html>
```